Window graphics for Kneadwell Haven

We need a new look for our store front. Attached is the current look and two samples of our logo.
the window measurements are (WxH in inches)
Top left: 72x32.5, each of the doors: 30x75.5, verical narrow window: 25.25x101, each of the two large windows on the right: 72x101

The new look will need to included the following content:

Content in each window:

Top left window: Our logo + 3817 (for the logo, try both short and long style)

Bottom left door: 614-555-0172 (don't make it too large. It must look clean and professional)

Right door: Logo

Vertical window right of right door: Every Day 10-9

Left large window:
Walk-Ins Welcome
Give the Gift of Massage!

Right large window:
Couples Massage
Hot Stone & Deep Tissue
Swedish & Foot

Target Market(s)

70% women, 30% men, middle class

Industry/Entity Type

Massage Center

Requirements
Must have
• A new fresh look to our store front. Easily read from a distance. The graphics and text must all be white only
Nice to have
• A clean look. See attached picture of a barber shop in our area.
Should not have
• Covering of whole window. Our landlord will not allow it.

```html
<!DOCTYPE html>
<html lang="en">
<head>
<meta charset="utf-8">
<title>Kneadwell Haven – Storefront Window Graphics</title>
<link rel="stylesheet" href="https://fonts.googleapis.com/css2?family=Poppins:wght@300;400;500;600;700&display=swap">
<style>
  :root {
    --page: #ffffff;
    --ink: #1c1c1c;
    --white: #ffffff;
    --glass-dark: #5d6169;
    --glass-mid: #8c9095;
    --glass-light: #b4b7ba;
    --glass-low: #9ea1a4;
    --sign-ink: #9a9da1;
  }
  * { box-sizing: border-box; margin: 0; padding: 0; }
  html, body {
    width: 1200px; height: 1000px; overflow: hidden;
    background: var(--page);
    font-family: "Poppins", sans-serif;
    color: var(--white);
  }
  .storefront { position: relative; width: 1200px; height: 1000px; }

  .window {
    position: absolute;
    background: linear-gradient(160deg, var(--glass-dark) 0%, var(--glass-mid) 18%, var(--glass-light) 45%, var(--glass-low) 100%);
  }
  .window--wide {
    background: linear-gradient(115deg, var(--glass-dark) 0%, var(--glass-mid) 14%, var(--glass-light) 38%, #a5a8ab 70%, var(--glass-low) 100%);
  }
  .window--door {
    background: linear-gradient(200deg, var(--glass-dark) 0%, var(--glass-mid) 14%, var(--glass-light) 40%, #a6a9ac 75%, var(--glass-low) 100%);
  }

  .top-left   { left: 191px; top: 319px; width: 237px; height: 107px; }
  .door-left  { left: 191px; top: 433px; width: 99px;  height: 248px; }
  .door-right { left: 329px; top: 433px; width: 99px;  height: 248px; }
  .hours-strip{ left: 435px; top: 319px; width: 83px;  height: 332px; }
  .large-left { left: 526px; top: 319px; width: 237px; height: 332px; }
  .large-right{ left: 772px; top: 319px; width: 237px; height: 332px; }

  .lockup {
    position: absolute; left: 0; right: 0; top: 50px;
    display: flex; align-items: center; justify-content: center; gap: 7px;
  }
  .brand-name { font-weight: 600; font-size: 10px; letter-spacing: 0.1px; white-space: nowrap; }
  .divider { width: 1px; height: 14px; background: var(--white); }
  .unit-number { font-weight: 500; font-size: 12.5px; letter-spacing: 0.5px; }

  .door-text {
    position: absolute; left: 0; right: 0; top: 121px;
    text-align: center; font-weight: 500; font-size: 8.5px; letter-spacing: 0.3px;
  }
  .door-text.brand-name { font-size: 9px; font-weight: 600; }

  .open-sign { position: absolute; left: 21px; top: 73px; }
  .hours {
    position: absolute; left: 0; right: 0; top: 124px; text-align: center;
  }
  .hours__days { font-weight: 600; font-size: 16px; line-height: 19px; }
  .hours__time { font-weight: 600; font-size: 23px; margin-top: 7px; letter-spacing: 0.5px; }

  .headline-top {
    position: absolute; left: 14px; top: 51px;
    font-weight: 600; font-size: 13.5px; letter-spacing: 0.1px;
  }
  .gift { position: absolute; left: 14px; top: 245px; line-height: 24px; }
  .gift__lead { font-weight: 300; font-size: 20px; }
  .gift__main { font-weight: 600; font-size: 20px; }

  .services {
    position: absolute; left: 16px; top: 243px; list-style: none;
    font-weight: 600; font-size: 14.5px; line-height: 18px;
  }

  .presentation-note {
    position: absolute; left: 0; right: 0; top: 862px; text-align: center;
    color: var(--ink); font-size: 9.5px; font-weight: 400;
  }
</style>
</head>
<body>
<main class="storefront">

  <section class="window window--wide top-left">
    <div class="lockup">
      <span class="brand-name">Kneadwell Haven</span>
      <span class="divider"></span>
      <svg width="12" height="12" viewBox="0 0 12 12" aria-hidden="true">
        <rect width="12" height="12" rx="1.5" fill="#fff"/>
        <path d="M6 2.3a2.4 2.4 0 0 0-2.4 2.4c0 1.8 2.4 4.6 2.4 4.6s2.4-2.8 2.4-4.6A2.4 2.4 0 0 0 6 2.3z" fill="#a3a6a9"/>
        <circle cx="6" cy="4.7" r="0.9" fill="#fff"/>
      </svg>
      <span class="unit-number">3817</span>
    </div>
  </section>

  <section class="window window--door door-left">
    <p class="door-text">614-555-0172</p>
  </section>

  <section class="window window--door door-right">
    <p class="door-text brand-name">Kneadwell Haven</p>
  </section>

  <section class="window hours-strip">
    <svg class="open-sign" width="40" height="36" viewBox="0 0 40 36" aria-hidden="true">
      <path d="M10 12 L20 3 L30 12" fill="none" stroke="#fff" stroke-width="1.6"/>
      <circle cx="20" cy="3.5" r="3" fill="#fff"/>
      <rect x="1" y="13" width="38" height="22" rx="3" fill="#fff"/>
      <text x="20" y="28.5" text-anchor="middle" font-family="Poppins, sans-serif" font-weight="600" font-size="10" fill="#9a9da1">OPEN</text>
    </svg>
    <div class="hours">
      <p class="hours__days">Every<br>Day</p>
      <p class="hours__time">10-9</p>
    </div>
  </section>

  <section class="window window--wide large-left">
    <h2 class="headline-top">WALK-INS WELCOME</h2>
    <p class="gift">
      <span class="gift__lead">Give the</span><br>
      <span class="gift__main">Gift of Massage!</span>
    </p>
  </section>

  <section class="window window--wide large-right">
    <ul class="services">
      <li>Couples Massage</li>
      <li>Hot Stone &amp; Deep Tissue</li>
      <li>Swedish &amp; Foot</li>
    </ul>
  </section>

  <p class="presentation-note">This Mock-Up is for presentation purposes only. Actual files will be flat against a white background.</p>
</main>
</body>
</html>
```